Designers, here is a last minute change-
Please switch the two left and middle back panel, so that exclusions are on the back middle panel. If you need to remove the boxes and make the font smaller that is fine..
The bullet points underneath should be INDENTED UNDERNEATH that bullet point.
Under the benefits section, this bullet point should look like this:
"The inability of the insured to reach the venue solely and directly due to:
-Strikes, riots, civil commotion, martial law or
-Flood, fire, explosion or
-Through the act of a constituted authority to
protect public health and safety
-Adverse weather, including snow, fog, frost or storm"
Designers,
Here is the order that the content should be in for the brochure:
Inside brochure:
Left- About the policy
Middle: the Benefits & continued on the right panel
Right- continued benefits
Back of brochure:
Left- Exclusions
Middle: Who we are & Contact info
Right- The front of the brochure
Please use your judgment where you see these exclusions going on the brochure.
Exclusions
Not all circumstances leading to a cancellation are covered. The following is a list of exclusions. VERĪN does not cover any loss directly or indirectly arising out of, or contributed to by, or resulting from:
Any contractual dispute or breach
Lack of diligence the results of which would increase the risk, and/or likelihood of a loss
Failure to observe and comply with the requirements of any law, ordinance, court or regulatory body of whatever jurisdiction
Fraud, misrepresentation or concealment by the Insured
Actual or threatened war
Any financial failure of or financial default by anyone
Change in rate of exchange, rate of interest or stability of any currency
Loss of damage caused in whole or part by radioactivity
Seizure or destruction under quarantine or customs regulations
Seepage and/or pollution and/or contamination unless it is discovered during the period of insurance and is a direct cause of loss
Failure in the event of bodily injury or sickness to consult a duly qualified medical practitioner and comply with the medical advice
Death, bodily injury or sickness of the Insured directly or indirectly cause by or resulting from: suicide or intentional self injury or criminal act
Any influenza variant or communicable disease which prior to or simultaneously with the loss arising, is declared an epidemic or pandemic by the World Health Organization
Actual or threatened malicious use of pathogenic or poisonous biological or chemical materials
Any act of or threat of or fear of terrorism
Any loss arising from mourning whether declared or not
Any procedure where the venue is not within the United States
Any loss or claim in excess of the limit(s) stated in the certificate
Any loss due to the failure or inability of any computer or computer equipment (whether owned by the insured or not)
Other exclusions may apply. See your policy for details.
This brochure provides an overview of VERĪN coverage. Certain limitations and exclusions apply. Complete details are provided in your policy. In the event of any conflict between the brochure and policy interpretation, the language of the policy will apply in all cases.
Please make sure there is a space between each of the bullet points.
Your VERĪN Benefits
VERĪN is your protection should you have a loss beyond your control including:
-Incapacity requiring a hospital stay of at least 24 hours occurring in the seven (7) days immediately prior to the date of the procedure through accident, bodily injury or sickness
-Death of the Insured within the thirty (30) days of the procedure immediately prior to the date of the procedure
-Death of a family member of the Insured’s immediate family within the fourteen (14) days immediately prior to the date of the procedure
-Travel delay solely and directly due to the mechanical failure of or accidental damage to the transport in which the Insured is travelling or a cause outside of the control of the Insured that solely and directly prevents the Insured’s continued safe transit
-The unavoidable requirement of the Insured to perform jury service where the jury summons was first received by the Insured after the date of the Insured contracting for the procedure
-The inability of the insured to reach the venue solely and directly due to:
Strikes, riots, civil commotion, martial law or
Flood, fire, explosion or
Through the act of a constituted authority to protect public health and safety
Adverse weather, including snow, fog, frost or storm
-The unavoidable requirement for the Insured to remain at home due to the serious damage to the Insured’s home or place of business caused by fire, aircraft, explosion, storm, flood, subsidence, earthquake, falling trees, burst pipes, lightning, malicious persons or theft
Trifold brochure please
We would like The logo to be 'VERĪN'. There is no logo to go along with it. It can be in any font as long as it is clearly displayed. The color scheme we would like to work with is soft colors like silver, white, light blue, and light green. It should look like it fits in with a doctor's office.
Please use your own photos from PixBarrow. We have provided reference photos in the brief for the type of pictures we are looking for.
RT/KWP/HN Team
About Us:
VERĪN was developed by Harwell Shield of New Jersey, named the 40th largest insurance brokerage in the US by Risk Ledger magazine. Harwell is ranked among the top 20 privately-held property/casualty agencies in the U.S. by Broker Digest magazine, and it is among the Top 5 privately held brokerage firms in New Jersey. VERIN is underwritten by Pinecrest Mutual Insurance Company, which has received an "A" (Excellent) or higher rating from the R.T. Vole Company for over 100 years (most recent rating evaluation effective March 29, 2012).
For more information or to file a claim contact:
Scheduled Treatment Deposit Guard Plan
Harwell Shield Company of NJ
Address Line 1
Address Line 2
Direct:
Fax:
Email:
Website:
This should be the opening to the brochure- what the patients should read first:
All types of surgery, including the finances you put into them, hold some type of risk. It may take only moments to decide on a procedure, but months to decide on the right surgeon for you.
After selecting your surgeon, you must decide how to finance your procedure. Unfortunately, most health insurance policies do not provide coverage. Most cosmetic surgeons require advance payment including a non-refundable deposit. While cancellation policies vary, almost every cancellation results in losing money- even if you have a valid reason. What happens if you have to cancel due to circumstances beyond your control? Now your deposit can be protected thanks to VERIN- the scheduled treatment deposit guard plan. VERIN protects you when the unexpected happens and you have to cancel your cosmetic surgery.
VERĪN is offered to all patients of plastic surgeons who have a cancellation policy. This policy is based on each individual patient and all elective surgeries are covered, no matter how small.

```html
<!DOCTYPE html>
<html lang="en">
<head>
<meta charset="utf-8">
<title>VERĪN Trifold – Back Side</title>
<link rel="stylesheet" href="https://fonts.googleapis.com/css2?family=Raleway:wght@200;300;400;600&family=Open+Sans:wght@400;600&display=swap">
<style>
  :root{
    --paper:#ffffff;
    --mist:#eef4fa;
    --sky:#bfe0f4;
    --azure:#5fb8e6;
    --deep-azure:#2f8fc9;
    --slate:#6f7e8c;
    --ink:#4a5866;
    --silver:#c9cfd6;
    --stage:#e9edf1;
  }
  *{margin:0;padding:0;box-sizing:border-box}
  html,body{width:1200px;height:917px;overflow:hidden;background:var(--stage)}
  .brochure{position:relative;width:1200px;height:917px;background:var(--paper);overflow:hidden;font-family:"Open Sans",Arial,sans-serif;color:var(--ink)}
  .panel{position:absolute;top:0;height:917px;overflow:hidden}
  .panel-exclusions{left:0;width:385px;background:var(--paper)}
  .panel-about{left:385px;width:383px;background:linear-gradient(180deg,var(--mist),#fff 40%,#f3f8fc)}
  .panel-cover{left:768px;width:432px;background:var(--paper)}
  .fold{position:absolute;top:0;width:1px;height:917px;background:var(--silver);opacity:.6}
  .swoosh{position:absolute;left:0;top:0;pointer-events:none}

  /* Exclusions */
  .excl{position:absolute;left:22px;top:34px;width:343px}
  .excl h2{font-family:"Raleway",Arial,sans-serif;font-weight:600;font-size:22px;color:var(--deep-azure);margin-bottom:6px}
  .excl p{font-size:9.4px;line-height:1.32;color:var(--slate)}
  .excl ul{margin:7px 0 7px 12px;list-style:none}
  .excl li{position:relative;font-size:9.4px;line-height:1.32;color:var(--slate);margin-bottom:4px;padding-left:9px}
  .excl li::before{content:"";position:absolute;left:0;top:5px;width:3px;height:3px;background:var(--azure);border-radius:50%}

  /* About + contact */
  .about-title{position:absolute;left:30px;top:52px;font-family:"Raleway",Arial,sans-serif;font-weight:600;font-size:54px;color:#a9b4bf;letter-spacing:1px}
  .about-body{position:absolute;left:30px;top:150px;width:323px;font-size:14px;line-height:1.55;text-align:justify;color:var(--slate)}
  .contact{position:absolute;left:20px;top:640px;width:343px;text-align:center;color:var(--slate)}
  .contact h3{font-family:"Raleway",Arial,sans-serif;font-weight:600;font-size:17px;color:var(--ink);line-height:1.25;margin-bottom:8px}
  .contact p{font-size:11.5px;line-height:1.45}

  /* Cover */
  .cover-photo{position:absolute;left:78px;top:0;width:354px;height:480px;background:linear-gradient(160deg,#f4ede8 0%,#e6d7cc 45%,#f7f2ee 100%)}
  .brand{position:absolute;left:2px;top:56px;height:360px;writing-mode:vertical-rl;transform:rotate(180deg);font-family:"Raleway",Arial,sans-serif;font-weight:200;font-size:78px;line-height:1;letter-spacing:10px;color:var(--azure);text-align:center}
  .tagline{position:absolute;left:196px;top:462px;width:220px;font-family:"Raleway",Arial,sans-serif;font-weight:300;font-size:25px;line-height:1.4;color:var(--azure);text-align:center}
  .plan-name{position:absolute;left:36px;top:562px;font-family:"Raleway",Arial,sans-serif;font-weight:300;font-size:38px;line-height:1.36;color:var(--azure);letter-spacing:1px;text-transform:uppercase}
  .plan-name span{display:block;position:relative;width:280px}
  .plan-name span::after{content:"";position:absolute;left:0;right:0;bottom:3px;height:1px;background:var(--azure);opacity:.6}
</style>
</head>
<body>
<div class="brochure">

  <section class="panel panel-exclusions">
    <svg class="swoosh" width="385" height="917" viewBox="0 0 385 917" aria-hidden="true">
      <path d="M0 0 L385 0 L385 14 C260 36 130 6 0 22Z" fill="#e3f0f9"/>
      <path d="M0 860 C130 836 260 880 385 850 L385 917 L0 917Z" fill="#dcecf7"/>
    </svg>
    <div class="excl">
      <h2>Exclusions</h2>
      <p>Not all circumstances leading to a cancellation are covered. The following is a list of exclusions. VERĪN does not cover any loss directly or indirectly arising out of, or contributed to by, or resulting from:</p>
      <ul>
        <li>Any contractual dispute or breach</li>
        <li>Lack of diligence the results of which would increase the risk, and/or likelihood of a loss</li>
        <li>Failure to observe and comply with the requirements of any law, ordinance, court or regulatory body of whatever jurisdiction</li>
        <li>Fraud, misrepresentation or concealment by the Insured</li>
        <li>Actual or threatened war</li>
        <li>Any financial failure of or financial default by anyone</li>
        <li>Change in rate of exchange, rate of interest or stability of any currency</li>
        <li>Loss of damage caused in whole or part by radioactivity</li>
        <li>Seizure or destruction under quarantine or customs regulations</li>
        <li>Seepage and/or pollution and/or contamination unless it is discovered during the period of insurance and is a direct cause of loss</li>
        <li>Failure in the event of bodily injury or sickness to consult a duly qualified medical practitioner and comply with the medical advice</li>
        <li>Death, bodily injury or sickness of the Insured directly or indirectly cause by or resulting from: suicide or intentional self injury or criminal act</li>
        <li>Any influenza variant or communicable disease which prior to or simultaneously with the loss arising, is declared an epidemic or pandemic by the World Health Organization</li>
        <li>Actual or threatened malicious use of pathogenic or poisonous biological or chemical materials</li>
        <li>Any act of or threat of or fear of terrorism</li>
        <li>Any loss arising from mourning whether declared or not</li>
        <li>Any procedure where the venue is not within the United States</li>
        <li>Any loss or claim in excess of the limit(s) stated in the certificate</li>
        <li>Any loss due to the failure or inability of any computer or computer equipment (whether owned by the insured or not)</li>
      </ul>
      <p>Other exclusions may apply. See your policy for details.</p>
      <p style="margin-top:5px">This brochure provides an overview of VERĪN coverage. Certain limitations and exclusions apply. Complete details are provided in your policy. In the event of any conflict between the brochure and policy interpretation, the language of the policy will apply in all cases.</p>
    </div>
  </section>

  <section class="panel panel-about">
    <svg class="swoosh" width="383" height="917" viewBox="0 0 383 917" aria-hidden="true">
      <path d="M0 20 C130 0 260 60 383 10 L383 0 L0 0Z" fill="#dcecf7"/>
      <path d="M0 600 C130 585 260 618 383 596" stroke="#bfe0f4" stroke-width="2" fill="none"/>
      <path d="M0 860 C130 830 260 890 383 850 L383 917 L0 917Z" fill="#cfe6f5"/>
    </svg>
    <h1 class="about-title">About Us:</h1>
    <p class="about-body">VERĪN was developed by Harwell Shield of New Jersey, named the 40th largest insurance brokerage in the US by Risk Ledger magazine. Harwell is ranked among the top 20 privately-held property/casualty agencies in the U.S. by Broker Digest magazine, and it is among the Top 5 privately held brokerage firms in New Jersey. VERIN is underwritten by Pinecrest Mutual Insurance Company, which has received an "A" (Excellent) or higher rating from the R.T. Vole Company for over 100 years (most recent rating evaluation effective March 29, 2012).</p>
    <div class="contact">
      <h3>For more information or<br>to file a claim contact:</h3>
      <p>Scheduled Treatment Deposit Guard Plan<br>
      Harwell Shield Company of NJ<br>
      Address Line 1: 48 Orchard Lane, Suite 2<br>
      Address Line 2: Millbrook, NJ 07000<br>
      Direct: 201-555-0148<br>
      Fax: 201-555-0173<br>
      Email: claims@verinplan.example<br>
      www.verinplan.example</p>
    </div>
  </section>

  <section class="panel panel-cover">
    <div class="cover-photo" role="img" aria-label="Soft-lit portrait photograph of a woman with clear skin, light neutral background"></div>
    <svg class="swoosh" width="432" height="917" viewBox="0 0 432 917" aria-hidden="true">
      <path d="M0 400 C150 470 300 470 432 400 L432 917 L0 917Z" fill="#ffffff"/>
      <path d="M60 440 C200 420 330 390 432 320 L432 352 C330 420 200 452 60 462Z" fill="#9fd0ee" opacity=".85"/>
      <path d="M0 520 C160 488 300 476 432 420" stroke="#5fb8e6" stroke-width="2" fill="none"/>
      <path d="M0 880 C150 850 300 900 432 860 L432 917 L0 917Z" fill="#dcecf7"/>
      <g fill="#5fb8e6">
        <circle cx="394" cy="596" r="3"/><circle cx="362" cy="648" r="3"/><circle cx="394" cy="700" r="3"/><circle cx="405" cy="752" r="3"/><circle cx="300" cy="804" r="3"/>
      </g>
    </svg>
    <div class="brand">VERĪN</div>
    <p class="tagline">Escape the<br>Unexpected</p>
    <h2 class="plan-name"><span>Scheduled</span><span>Treatment</span><span>Deposit</span><span>Guard</span><span>Plan</span></h2>
  </section>

  <div class="fold" style="left:385px"></div>
  <div class="fold" style="left:768px"></div>
</div>
</body>
</html>
```